Management Consultancy needs sharp professional services showcased in a brochure

We are a management consultancy specializing on contract management and conflict avoidance services requiring a professional brochure showcasing our services to prospective clients.

Attached are a selection of existing stationary and the colour scheme.

Further details on our company can be found at www.velmor-advisory-partners.com
Updates

Preference is for bi-fold, however, innovative tri-fold will be considered. Added Monday, August 7, 2017

Target Market(s)

Construction companies, consultants, developers, oil and gas service providers, NGO's, SME's.

Industry/Entity Type

Management

Requirements
Must have
• High degree of professionalism with eye catching, sharp detail. No frils.
• Colour scheme as per the attachments
• Font as per attachments - Century Gothic
• Details of our company and services
Nice to have
• Open to ideas, thinking along the lines of a car brochure type design.
• Bi-fold preferred, by trifold accepted if innovative.
Should not have
• Remove reference to the United Arab Emirates.
• No cartoon/clipart photos.

```html
<!DOCTYPE html>
<html lang="en">
<head>
<meta charset="utf-8">
<title>Velmor Advisory — Brochure Spread</title>
<link rel="stylesheet" href="https://fonts.googleapis.com/css2?family=Cinzel:wght@400;500&family=Open+Sans:wght@400;600;700&display=swap">
<style>
  :root {
    --navy: #1f3a5c;
    --navy-deep: #2b3146;
    --slate: #454c63;
    --red: #c0272d;
    --peach: #f2d2c6;
    --ink: #3b3b3b;
    --white: #ffffff;
  }
  html, body { margin: 0; padding: 0; overflow: hidden; background: var(--white); }
  .spread {
    position: relative; width: 1200px; height: 777px; overflow: hidden;
    background: var(--white); font-family: "Open Sans", Arial, sans-serif; color: var(--ink);
  }
  .abs { position: absolute; }
  .accent-shapes { position: absolute; inset: 0; width: 1200px; height: 777px; }

  /* Left page */
  .hero-panel {
    left: 0; top: 0; width: 600px; height: 250px;
    background: linear-gradient(120deg, #3a4057 0%, #2b3146 45%, #4b5269 100%);
  }
  .hero-title {
    left: 61px; top: 32px; width: 450px; margin: 0;
    font-family: "Cinzel", serif; font-weight: 400; font-size: 19px; line-height: 23.2px;
    color: var(--white); letter-spacing: 0;
  }
  .sector-list {
    left: 77px; top: 143px; margin: 0; padding: 0; list-style: none;
    color: var(--white); font-size: 12px; line-height: 16.5px;
  }
  .sector-list li { position: relative; padding-left: 19px; }
  .sector-list li::before {
    content: ""; position: absolute; left: 0; top: 6px; width: 5px; height: 5px;
    border-radius: 50%; background: var(--red);
  }
  .brand-name {
    left: 44px; top: 346px; margin: 0; font-size: 17px; font-weight: 600;
    color: var(--navy); white-space: nowrap;
  }
  .intro { left: 225px; top: 278px; width: 345px; }
  .body-copy p { margin: 0 0 12.8px; font-size: 9.4px; line-height: 12.8px; }
  .value { left: 139px; width: 420px; }
  .value h3 { margin: 0 0 1px; font-size: 12px; font-weight: 700; line-height: 16px; color: var(--navy); }
  .value.equality h3 { color: var(--red); }
  .value p { margin: 0 0 12.8px; font-size: 9.4px; line-height: 12.8px; }
  .value.integrity { top: 427px; }
  .value.equality { top: 522px; }
  .value.endurance { top: 655px; }

  /* Right page */
  .services-title {
    left: 653px; top: 30px; margin: 0; font-family: "Cinzel", serif; font-weight: 400;
    font-size: 28px; line-height: 36px; color: var(--red);
  }
  .services-intro { left: 653px; top: 72px; width: 508px; }
  .service-photo { left: 653px; width: 162px; }
  .service-photo.conflict { top: 238px; height: 74px; background: linear-gradient(90deg, #1a1c22, #f0f0f2 45%, #f0f0f2 55%, #1a1c22); }
  .service-photo.contract { top: 374px; height: 108px; background: radial-gradient(circle at 58% 45%, #d8d8d8 0%, #7a7a7a 35%, #1c1c1c 80%); }
  .service-block { left: 829px; width: 330px; }
  .service-block h3 { margin: 0 0 5px; font-size: 12px; font-weight: 700; line-height: 16px; color: var(--navy); }
  .service-block ul { margin: 0; padding: 0; list-style: none; }
  .service-block li { position: relative; padding-left: 24px; font-size: 9.4px; line-height: 18.5px; }
  .service-block li::before {
    content: ""; position: absolute; left: 8px; top: 7px; width: 4px; height: 4px;
    border-radius: 50%; background: var(--red);
  }
  .service-block.conflict { top: 237px; }
  .service-block.contract { top: 370px; }

  .reach-panel {
    left: 600px; top: 526px; width: 600px; height: 251px;
    background: linear-gradient(110deg, #2b3146 0%, #3c4259 50%, #2b3146 100%);
  }
  .reach-statement {
    left: 630px; top: 547px; width: 540px; margin: 0; text-align: center;
    color: var(--white); font-size: 12.6px; font-weight: 600; line-height: 16.6px;
  }
  .project { top: 635px; width: 78px; margin: 0; text-align: center; color: var(--white); }
  .project-photo { width: 78px; height: 77px; }
  .project-caption { width: 82px; margin: 5px -2px 0; font-size: 8.4px; line-height: 11.8px; }
  .project-caption strong { display: block; font-weight: 700; }
</style>
</head>
<body>
<main class="spread">
  <svg class="accent-shapes" viewBox="0 0 1200 777" aria-hidden="true">
    <polygon points="0,250 88,250 0,368" fill="#f2d2c6"/>
    <polygon points="1200,424 1200,526 1110,526" fill="#f2d2c6"/>
  </svg>

  <!-- Left page -->
  <div class="abs hero-panel" role="img" aria-label="Dim office interior with silhouetted people walking past large windows"></div>
  <h1 class="abs hero-title">We are an experienced contract and conflict advisory providing global contract performance solutions and conflict management to:</h1>
  <ul class="abs sector-list">
    <li>International development organisations;</li>
    <li>Construction industry;</li>
    <li>Oil and gas industry; and</li>
    <li>Government sectors.</li>
  </ul>

  <p class="abs brand-name">Velmor Advisory</p>

  <div class="abs intro body-copy">
    <p>We believe that there are three core values or Velmor Principles which must be adhered to for successful contract management and conflict resolution, these principles set the foundation for our services.</p>
    <p>With Velmor Advisory, we introduce into this continuous cycle our integrated accountability model.</p>
    <p>Therein, our symbol represents our principles of integrity, equality and endurance, with each value carrying an important role in delivery.</p>
  </div>

  <section class="abs value integrity">
    <h3>Integrity</h3>
    <p>We believe that "whoever walks in integrity, walks securely".</p>
    <p>Where one is guided by integrity, there lies honesty, which leads to the foundation of success through the building of strong character, be it corporate or individual , eradicating deceit, and ensuring that the right route is followed, regardless of consequence.</p>
  </section>
  <section class="abs value equality">
    <h3>Equality</h3>
    <p style="margin:0">As Aldric Venn said, "Before God, we are all equally wise, and equally foolish".</p>
    <p>The existence of equality amongst parties promotes our own individual interests, aiding their preservation and acceptance. In the establishment of equality, we reduce the inequalities, resulting in mutuality and respect between participants.</p>
    <p>This therefore advances unity, a key requirement in any contractual engagement, providing cooperation and enhancement of knowledge of expectation and aiding in meeting these expectations.</p>
  </section>
  <section class="abs value endurance">
    <h3>Endurance</h3>
    <p>Endurance is a fundamental building block of character, which grows in the face of tribulation. Every relationship, be it contractual or not carries tribulation.</p>
    <p>In the contractual relationship context, regardless of what is contained in the contract, parties perceptions or circumstances change, often due to misrepresentation, or awareness of obligation, which may lead to tangential deviation from the perfect contractual flow.</p>
  </section>

  <!-- Right page -->
  <h2 class="abs services-title">Our Services</h2>
  <div class="abs services-intro body-copy">
    <p>Every contract has at least two parties; every party has a goal, and every goal matters. Each party must work in equilibrium as a contractual partnership or alliance, it is on this premise we aim to deliver truly mutual agreements, maintaining the contract integrity from inception through the contract life, and where we are not party to the original agreement, we provide effective solutions to contractual conflict via our unique mediation methodology at all positions of the conflict cycle and aim to enhance all aspects of contract performance by effective audit and management.</p>
    <p>We believe that a proactive approach to contract management creates transparency and trust, and maintains relationships and builds on them for the future whilst cultivating significant value to your business transactions and addressing real and relevant issues, providing and implementing effective solutions. We believe that avoidance of contractual conflict and timely resolution on escalation is paramount in the effectiveness of any agreement.</p>
  </div>

  <div class="abs service-photo conflict" role="img" aria-label="Two hands bringing together matching puzzle pieces against a white background"></div>
  <section class="abs service-block conflict">
    <h3>Conflict Advisory</h3>
    <ul>
      <li>Restoration and Mediation Services.</li>
      <li>Shuttle Diplomacy Services and In Persona Intermediary Services.</li>
      <li>Negotiation Support Services.</li>
      <li>Workplace Mediation Services</li>
    </ul>
  </section>

  <div class="abs service-photo contract" role="img" aria-label="Row of light bulbs on a dark surface with one bulb glowing"></div>
  <section class="abs service-block contract">
    <h3>Contract Advisory</h3>
    <ul>
      <li>Contract Troubleshooting.</li>
      <li>Contracts Audit Services and Performance Management.</li>
      <li>Strategic Review &amp; Risk Assessment.</li>
      <li>Contract Fraud Investigation.</li>
    </ul>
  </section>

  <div class="abs reach-panel" role="img" aria-label="Darkened photo of a handshake behind the project gallery"></div>
  <p class="abs reach-statement">At Velmor Advisory, we pride ourselves on our versatility, providing a global reach with a local relationship; we ensure that our clients get the boutique service they deserve. Providing a multitude of support services in an array of industries and locations, our clients' interests are always at the forefront of our minds.</p>

  <figure class="abs project" style="left:687px">
    <div class="project-photo" role="img" aria-label="Aerial view of island construction site by the sea" style="background:linear-gradient(160deg,#7fa9b8,#c9b89a 55%,#a88f6c)"></div>
    <figcaption class="project-caption"><strong>Construction</strong>Island Resort Development</figcaption>
  </figure>
  <figure class="abs project" style="left:776px">
    <div class="project-photo" role="img" aria-label="Aerial view of a multi-use shipyard facility on the coast" style="background:linear-gradient(170deg,#9bb0bd,#5f7788 50%,#b5a58a)"></div>
    <figcaption class="project-caption"><strong>Construction</strong>Multi-Use Shipyard Facility, Coastal Zone</figcaption>
  </figure>
  <figure class="abs project" style="left:866px">
    <div class="project-photo" role="img" aria-label="Offshore drilling rigs moored in a shipyard" style="background:linear-gradient(180deg,#c9ccd0,#a3503f 55%,#6d7276)"></div>
    <figcaption class="project-caption"><strong>Shipyard</strong>Offshore Drilling Unit, Marine Yard</figcaption>
  </figure>
  <figure class="abs project" style="left:955px">
    <div class="project-photo" role="img" aria-label="Offshore distribution platform and jetty at sea" style="background:linear-gradient(180deg,#b8c4cc,#5b7a8e 60%,#3c5566)"></div>
    <figcaption class="project-caption"><strong>Fabrication</strong>Offshore Distribution Platform, Basra, Iraq</figcaption>
  </figure>
  <figure class="abs project" style="left:1044px">
    <div class="project-photo" role="img" aria-label="Aerial view of a port warehousing and yard facility" style="background:linear-gradient(150deg,#a9b7c0,#b86a4a 55%,#8a6b55)"></div>
    <figcaption class="project-caption"><strong>Construction</strong>Port Warehousing and Yard Facility, Luanda, Angola</figcaption>
  </figure>
</main>
</body>
</html>
```